Letterhead for a German Distribution/Manufacturing Company

We need a professional Letterhead in a unique Design.
not to playful.
The Letterhead has to show show that we are a international company with headquater in Germany.
all details like adress, Vat Tax Number, Bank Accout, Eori, email, Company number has to be on the Letterhead.
for example use: VAT TAX DE5704168 Bank Account: Norrfeld Bank IBAN DE421705238ß310482 Swift: KOLV3154802 EORI 3041296587 Company Number: HRB 61508 Adress: VOLTRINA UG Amsel Strasse 7 Postal Code 04683 City Feldwinkel Country: Germany Email: info@voltrina-example.com
the design can be colored but doesnt have to be
Industry/Entity Type
Manufacturing and international distribution
Requirements
Must have
- show that we are a international company with headquater in Germany. our company infos and logo

```html
<!DOCTYPE html>
<html lang="en">
<head>
<meta charset="utf-8">
<title>VOLTRINA Letterhead</title>
<link rel="stylesheet" href="https://fonts.googleapis.com/css2?family=Poppins:wght@400;500;600;700&display=swap">
<style>
  :root {
    --ink: #222222;
    --paper: #ffffff;
    --backdrop: #f3f3f3;
    --tone-1: #222222;
    --tone-2: #4d4d4d;
    --tone-3: #636363;
    --tone-4: #7b7b7b;
    --tone-5: #a5a5a5;
    --tone-6: #c4c4c4;
    --flag-black: #000000;
    --flag-red: #dd0000;
    --flag-gold: #ffce00;
  }
  * { margin: 0; padding: 0; box-sizing: border-box; }
  html, body {
    width: 1200px; height: 2210px; overflow: hidden;
    background: var(--backdrop);
    font-family: "Poppins", sans-serif;
    color: var(--ink);
  }
  .letterhead {
    position: absolute; left: 80px; top: 370px;
    width: 1040px; height: 1472px;
    background: var(--paper);
    box-shadow: 0 20px 60px rgba(0,0,0,0.22);
    overflow: hidden;
  }
  .header-cap {
    position: absolute; left: 0; top: 45px; width: 96px; height: 88px;
    background: var(--ink); border-radius: 0 44px 44px 0;
  }
  .brand {
    position: absolute; left: 122px; top: 45px; height: 88px;
    display: flex; align-items: center; gap: 14px;
  }
  .brand-dot { width: 34px; height: 34px; border-radius: 50%; background: var(--ink); }
  .brand-name { font-size: 44px; font-weight: 400; letter-spacing: 0.5px; }
  .header-band {
    position: absolute; left: 435px; top: 45px; width: 605px; height: 88px;
    background: var(--ink); border-radius: 44px 0 0 44px;
    color: #fff;
  }
  .header-claim {
    position: absolute; left: 50px; top: 14px;
    font-size: 26px; font-weight: 500; line-height: 30px;
  }
  .flag { position: absolute; left: 430px; top: 19px; width: 76px; height: 49px; }
  .contact {
    position: absolute; right: 47px; text-align: right;
    font-size: 18px; font-weight: 500; line-height: 21px;
    display: flex; align-items: center; gap: 22px;
  }
  .contact-address { top: 167px; }
  .contact-email { top: 240px; }
  .contact-icon { width: 25px; height: 25px; flex: none; }
  .recipient { position: absolute; left: 45px; top: 318px; }
  .recipient-to { font-size: 25px; line-height: 32px; }
  .recipient-name { font-size: 38px; font-weight: 700; line-height: 46px; letter-spacing: 1px; }
  .recipient-role { font-size: 28px; line-height: 34px; }
  .letter-body {
    position: absolute; left: 45px; top: 480px; width: 947px;
    font-size: 17px; line-height: 21px;
  }
  .salutation { font-size: 21px; margin-left: 2px; margin-bottom: 26px; }
  .letter-body p.copy { text-align: justify; margin-bottom: 31px; }
  .signature {
    position: absolute; left: 45px; top: 1052px; width: 262px; height: 56px;
    background: linear-gradient(90deg, #e6e6e6, #f4f4f4);
    border-radius: 4px;
  }
  .signer { position: absolute; left: 47px; top: 1116px; font-size: 17.5px; line-height: 20px; }
  .signer-name { font-weight: 700; }
  .footer-rule {
    position: absolute; top: 1219px; height: 1.5px; background: var(--ink);
  }
  .footer-rule-left { left: 0; width: 62px; }
  .footer-rule-right { left: 146px; width: 846px; }
  .footer-mark {
    position: absolute; left: 62px; top: 1211px; width: 84px;
    text-align: center; font-size: 13px; font-weight: 600; letter-spacing: 0.5px;
  }
  .footer-col {
    position: absolute; top: 1262px;
    font-size: 17.5px; line-height: 26px;
  }
  .footer-col dt { font-weight: 600; }
  .footer-col dd { font-weight: 400; }
  .footer-col .strong { font-weight: 600; }
  .col-finance { left: 45px; }
  .col-trade { left: 543px; }
  .col-registry { left: 808px; }
  .footer-divider {
    position: absolute; top: 1252px; width: 1px; height: 113px; background: var(--ink);
  }
  .divider-a { left: 468px; }
  .divider-b { left: 732px; }
  .tone-bar {
    position: absolute; left: 0; bottom: 0; width: 100%; height: 71px; display: flex;
  }
  .tone-bar span { flex: 1; }
</style>
</head>
<body>
<main class="letterhead">
  <div class="header-cap"></div>
  <div class="brand">
    <span class="brand-dot"></span>
    <span class="brand-name">VOLTRINA</span>
  </div>
  <div class="header-band">
    <p class="header-claim">International company,<br>Headquarter in Germany</p>
    <svg class="flag" viewBox="0 0 76 49" aria-label="Flag of Germany" role="img">
      <rect width="76" height="16.4" y="0" fill="var(--flag-black)"/>
      <rect width="76" height="16.4" y="16.3" fill="var(--flag-red)"/>
      <rect width="76" height="16.4" y="32.6" fill="var(--flag-gold)"/>
    </svg>
  </div>

  <div class="contact contact-address">
    <span>VOLTRINA UG Amsel Strasse 7<br>Postal Code 04683 City Feldwinkel</span>
    <svg class="contact-icon" viewBox="0 0 25 25" aria-hidden="true">
      <rect width="25" height="25" rx="6" fill="var(--ink)"/>
      <path d="M12.5 5a5 5 0 0 0-5 5c0 3.6 5 9 5 9s5-5.4 5-9a5 5 0 0 0-5-5z" fill="#fff"/>
      <circle cx="12.5" cy="10" r="2" fill="var(--ink)"/>
    </svg>
  </div>
  <div class="contact contact-email">
    <span>info@voltrina-example.com</span>
    <svg class="contact-icon" viewBox="0 0 25 25" aria-hidden="true">
      <rect width="25" height="25" rx="6" fill="var(--ink)"/>
      <rect x="5" y="7.5" width="15" height="10" rx="1.5" fill="#fff"/>
      <path d="M5.5 8.5l7 5 7-5" stroke="var(--ink)" stroke-width="1.5" fill="none"/>
    </svg>
  </div>

  <section class="recipient">
    <p class="recipient-to">TO</p>
    <p class="recipient-name">JOHN SMITH</p>
    <p class="recipient-role">Marketing Manager</p>
  </section>

  <section class="letter-body">
    <p class="salutation">Dear Sir,</p>
    <p class="copy">Lorem Ipsum is simply dummy text of the printing and typesetting industry. Lorem Ipsum has been the industry's standard dummy text ever since the 1500s, when an unknown printer took a galley of type and scrambled it to make a type specimen book. It has survived not only five centuries, but also the leap into electronic typesetting, remaining essentially unchanged. It was popularised in the 1960s with the release of Typeforma sheets containing Lorem Ipsum passages, and more recently with desktop publishing software like Quillset Layout including versions of Lorem Ipsum.</p>
    <p class="copy">It is a long established fact that a reader will be distracted by the readable content of a page when looking at its layout. The point of using Lorem Ipsum is that it has a more-or-less normal distribution of letters, as opposed to using 'Content here, content here', making it look like readable English. Many desktop publishing packages and web page editors now use Lorem Ipsum as their default model text, and a search for 'lorem ipsum' will uncover many web sites still in their infancy. Various versions have evolved over the years, sometimes by accident, sometimes on purpose (injected humour and the like).</p>
    <p class="copy">Contrary to popular belief, Lorem Ipsum is not simply random text. It has roots in a piece of classical Latin literature from 45 BC, making it over 2000 years old. Arvid Lenhart, a Latin professor at Marlow Ridge College in Eastvale, looked up one of the more obscure Latin words, consectetur, from a Lorem Ipsum passage, and going through the cites of the word in classical literature, discovered the undoubtable source. Lorem Ipsum comes from sections 1.10.32 and 1.10.33 of an old treatise (The Extremes of Good and Evil) by Quintor, written in 45 BC. This book is a treatise on the theory of ethics, very popular during the Renaissance. The first line of Lorem Ipsum, "Lorem ipsum dolor sit amet..", comes from section 1.10.32.</p>
  </section>

  <div class="signature" role="img" aria-label="Handwritten signature of John Smith"></div>
  <div class="signer">
    <p class="signer-name">JOHN SMITH</p>
    <p>Marketing Manager</p>
  </div>

  <div class="footer-rule footer-rule-left"></div>
  <div class="footer-mark">VOLTRINA</div>
  <div class="footer-rule footer-rule-right"></div>

  <dl class="footer-col col-finance">
    <dt>VAT TAX</dt>
    <dd>DE5704168</dd>
    <dt>Bank Account:</dt>
    <dd>Norrfeld Bank IBAN DE421705238ß310482</dd>
  </dl>
  <div class="footer-divider divider-a"></div>
  <dl class="footer-col col-trade">
    <dt>Swift:</dt>
    <dd>KOLV3154802</dd>
    <dt>EORI</dt>
    <dd class="strong">3041296587</dd>
  </dl>
  <div class="footer-divider divider-b"></div>
  <dl class="footer-col col-registry">
    <dt>Company Number:</dt>
    <dd>HRB 61508</dd>
    <dt>Country:</dt>
    <dd>Germany</dd>
  </dl>

  <div class="tone-bar" aria-hidden="true">
    <span style="background:var(--tone-1)"></span>
    <span style="background:var(--tone-2)"></span>
    <span style="background:var(--tone-3)"></span>
    <span style="background:var(--tone-4)"></span>
    <span style="background:var(--tone-5)"></span>
    <span style="background:var(--tone-6)"></span>
  </div>
</main>
</body>
</html>
```